Corporate Notepads

We currently have a basic notepad with our logo and icon at the top along with contact information at the bottom. We want to come up with something more creative and jazz it up a bit. We are looking for unique ideas to make the notepads look nice and corporate possibly with watermarked look. We will take any ideas and choose the one that works best for the look. We have a website where you can get ideas about our company. Attached is the current simple notepad design we have right now.

```html
<!DOCTYPE html>
<html lang="en">
<head>
<meta charset="UTF-8">
<title>Hartwell Construction Notepad</title>
<link href="https://fonts.googleapis.com/css2?family=Barlow+Condensed:wght@600&family=Open+Sans:wght@600;700&display=swap" rel="stylesheet">
<style>
  :root {
    --backdrop: #ece5da;
    --paper: #eef0f3;
    --paper-shade: #dfe2e7;
    --navy: #2b4a93;
    --ink: #1c1d22;
    --band-text: #dfe5f3;
    --watermark: #cdd2dd;
  }
  * { margin: 0; padding: 0; box-sizing: border-box; }
  html, body {
    width: 1200px;
    height: 960px;
    overflow: hidden;
    background: var(--backdrop);
  }
  .canvas {
    position: relative;
    width: 1200px;
    height: 960px;
  }
  .sheet {
    position: absolute;
    left: 255px;
    top: 30px;
    width: 690px;
    height: 900px;
    background: linear-gradient(160deg, var(--paper) 0%, var(--paper-shade) 100%);
    overflow: hidden;
  }
  .brand {
    position: absolute;
    top: 62px;
    left: 0;
    width: 100%;
    display: flex;
    justify-content: center;
    align-items: center;
    gap: 10px;
  }
  .brand-square {
    width: 66px;
    height: 66px;
    background: var(--navy);
  }
  .brand-name {
    font-family: "Barlow Condensed", sans-serif;
    font-weight: 600;
    color: var(--navy);
    font-size: 38px;
    line-height: 0.9;
    letter-spacing: 0.5px;
  }
  .brand-name span { display: block; font-size: 26px; letter-spacing: 1px; }
  .watermark {
    position: absolute;
    left: 0;
    top: 360px;
    width: 100%;
    text-align: center;
    font-family: "Barlow Condensed", sans-serif;
    font-weight: 600;
    font-size: 130px;
    line-height: 1;
    letter-spacing: 4px;
    color: var(--watermark);
  }
  .contact {
    position: absolute;
    top: 831px;
    width: 100%;
    text-align: center;
    font-family: "Open Sans", sans-serif;
    font-weight: 600;
    font-size: 15px;
    letter-spacing: 1px;
    color: var(--ink);
  }
  .contact .label { color: var(--navy); }
  .services-band {
    position: absolute;
    left: 0;
    bottom: 0;
    width: 100%;
    height: 36px;
    background: var(--navy);
    display: flex;
    justify-content: center;
    align-items: center;
    font-family: "Open Sans", sans-serif;
    font-weight: 700;
    font-size: 14px;
    letter-spacing: 2px;
    color: var(--band-text);
  }
</style>
</head>
<body>
<div class="canvas">
  <div class="sheet">
    <header class="brand">
      <div class="brand-square"></div>
      <div class="brand-name">HARTWELL<span>CONSTRUCTION</span></div>
    </header>

    <div class="watermark" aria-hidden="true">HARTWELL</div>

    <p class="contact">hartwellconstruction.com | <span class="label">Tel:</span> 555-014-2298</p>
    <footer class="services-band">CIVIL • INDUSTRIAL • COMMERCIAL</footer>
  </div>
</div>
</body>
</html>
```